Medical group practice

We need a flyer design incorporating the three doctors in the practice, there is a general practitioner, ophthalmologist and an obstetrician & Gynaecologist. see the attached file for the concept. will leave the colour design up to you

Target Market(s)

general public

Industry/Entity Type

Health Care

Colors

Designer to choose colors to be used in the design.

Requirements
Must have
• logos included in attachement

```html
<!DOCTYPE html>
<html lang="en">
<head>
<meta charset="utf-8">
<title>Northvale Medical Flyer</title>
<link href="https://fonts.googleapis.com/css2?family=Cinzel:wght@500&family=Open+Sans:wght@400;700&family=Lato:wght@400;700&display=swap" rel="stylesheet">
<style>
:root{
  --red:#d7262e;
  --grey:#b9b9bb;
  --dark:#444446;
  --ink:#1d1d1f;
  --bg:#e4e4e6;
  --white:#ffffff;
}
html,body{margin:0;width:1200px;height:1200px;overflow:hidden;background:var(--bg);}
.flyer{position:absolute;left:255px;top:75px;width:949px;height:1331px;background:var(--white);
  transform:scale(0.8);transform-origin:top left;overflow:hidden;font-family:"Lato",sans-serif;color:var(--ink);
  box-shadow:0 6px 18px rgba(0,0,0,.25);}
.abs{position:absolute;}
.brand-mark{left:40px;top:60px;width:90px;height:90px;border-radius:50%;background:var(--red);}
.brand-name{left:161px;top:28px;font-family:"Cinzel",serif;font-size:32px;letter-spacing:1px;color:var(--ink);
  border-bottom:1.5px solid var(--ink);padding-bottom:2px;white-space:nowrap;}
.tagline{left:161px;top:66px;font-family:"Open Sans",sans-serif;font-size:28px;white-space:nowrap;}
.address{left:194px;top:106px;font-size:16px;font-weight:700;line-height:21px;}
.address svg{vertical-align:-3px;margin-right:6px}
.team-photo{left:560px;top:100px;width:389px;height:250px;
  background:linear-gradient(90deg,#ffffff 0%,#3d78c4 22%,#4f86d0 55%,#eef0f4 78%,#2a5fb0 100%);}
.waves{left:0;top:0;}
.practice-name{width:170px;text-align:center;font-weight:700;font-size:17px;color:#1f4f8e;line-height:21px;}
.doctor{left:225px;}
.doctor h2{margin:0;font-family:"Open Sans",sans-serif;font-size:22px;color:var(--red);font-weight:700;}
.doctor p{margin:6px 0 0;font-size:17px;font-weight:700;line-height:21px;}
.doctor .email{font-size:16px;margin-top:8px}
.doctor .email svg{vertical-align:-2px;margin-right:6px}
.services{list-style:none;margin:0;padding:0;font-size:15.5px;}
.services li{position:relative;padding-left:22px;height:37px;line-height:18px;}
.services li::before{content:"";position:absolute;left:2px;top:2px;width:6px;height:11px;border:solid var(--ink);
  border-width:0 2.5px 2.5px 0;transform:rotate(40deg);}
.services li.tall{height:56px}
.col-head{font-weight:700;font-size:17px;margin:0 0 14px;}
.footer-contacts{left:35px;top:1112px;color:var(--white);}
.contact{display:flex;gap:14px;margin-bottom:30px;font-family:"Open Sans",sans-serif;font-size:18px;line-height:20px;font-weight:700;}
.contact span{display:block;font-weight:400}
.hours{left:451px;top:1073px;width:220px;height:220px;border-radius:50%;background:var(--white);
  border:5px solid var(--red);text-align:center;box-sizing:border-box;}
.hours h3{margin:0;color:var(--red);font-family:"Open Sans",sans-serif;font-size:19px;font-weight:700;}
.hours p{margin:6px 0 0;font-size:15px;font-weight:700;line-height:19px;}
</style>
</head>
<body>
<div class="flyer">
  <div class="abs team-photo" role="img" aria-label="Photo of three smiling doctors in white coats and blue scrubs holding clipboards"></div>

  <svg class="abs waves" width="949" height="1331" viewBox="0 0 949 1331">
    <path d="M0 350 C250 420 560 250 949 330 L949 520 L0 520Z" fill="var(--white)"/>
    <path d="M0 345 C260 410 560 240 949 320 L949 360 C600 270 300 440 0 380Z" fill="var(--grey)"/>
    <path d="M0 316 C270 390 560 210 949 280 L949 335 C600 250 300 420 0 355Z" fill="var(--red)"/>
    <path d="M0 1085 C200 1040 380 1070 500 1170 L600 1275 C760 1275 860 1265 949 1240 L949 1331 L0 1331Z" fill="var(--dark)"/>
    <path d="M0 1085 C200 1040 380 1070 500 1170" stroke="var(--red)" stroke-width="6" fill="none"/>
    <path d="M600 1215 C760 1212 880 1200 949 1170 L949 1205 C860 1235 760 1245 600 1240Z" fill="var(--grey)"/>
    <path d="M600 1240 C760 1245 860 1235 949 1205 L949 1240 C860 1265 760 1275 600 1275Z" fill="var(--red)"/>
  </svg>

  <div class="abs brand-mark"></div>
  <div class="abs brand-name">NORTHVALE MEDICAL</div>
  <div class="abs tagline">Your Health is our Priority</div>
  <div class="abs address">42 Harbour Lane, Eastport, St. Kitts<br>
    <svg width="16" height="16" viewBox="0 0 16 16"><circle cx="8" cy="8" r="7" fill="none" stroke="currentColor" stroke-width="1.2"/><path d="M5.5 4.2l1.3 1.6-.8 1c.5 1 1.2 1.8 2.2 2.3l1-.8 1.6 1.3-.9 1.2c-2.6-.4-4.9-2.7-5.3-5.3z" fill="currentColor"/></svg>(555) 210 4410 / 4411</div>

  <div class="abs practice-name" style="left:25px;top:495px">Harbourside Family Practice</div>
  <div class="abs doctor" style="top:476px">
    <h2>Dr. Colin Marsh, MD</h2>
    <p>General Practitioner</p>
    <p class="email"><svg width="20" height="14" viewBox="0 0 20 14"><rect width="20" height="14" fill="var(--ink)"/><path d="M0 0l10 8 10-8" stroke="#fff" stroke-width="1.5" fill="none"/></svg>colin.marsh.doc@example.com</p>
  </div>
  <ul class="abs services" style="left:526px;top:458px">
    <li>General Checks</li><li>Annual Check ups</li><li>Wound Care/Dressings</li><li>Incision &amp; Drainage</li>
  </ul>
  <ul class="abs services" style="left:739px;top:458px">
    <li>Suturing lacerations</li><li>Pain Injections</li><li>Glucose checks</li><li>Foreign Body Removal</li>
  </ul>

  <div class="abs practice-name" style="left:25px;top:706px;color:#6a1b8a">Clearview Eye Care</div>
  <div class="abs doctor" style="top:688px">
    <h2>Dr. Elena R. Castillo</h2>
    <p>MD. Surgeon Ophthalmologist</p>
    <p class="email"><svg width="20" height="14" viewBox="0 0 20 14"><rect width="20" height="14" fill="var(--ink)"/><path d="M0 0l10 8 10-8" stroke="#fff" stroke-width="1.5" fill="none"/></svg>elena.eyes@example.com</p>
  </div>
  <ul class="abs services" style="left:526px;top:682px">
    <li>Eyes disease examination</li><li>Surgery of Pterygium</li><li>Cataract</li><li>Glaucoma</li>
  </ul>
  <div class="abs" style="left:739px;top:680px">
    <p class="col-head">Emergency</p>
    <ul class="services">
      <li>Conjunctivitis</li><li>Traumatism</li><li class="tall">Foreign body and<br>more...</li>
    </ul>
  </div>

  <div class="abs practice-name" style="left:25px;top:895px;color:#1b3f8a">Bloom Women's Health</div>
  <div class="abs doctor" style="top:875px">
    <h2>Dr. Vikram Desai</h2>
    <p>BMedSci, MBBS, DM (O&amp;G)<br>FACOG, Obstetrician<br>&amp; Gynaecologist</p>
    <p class="email"><svg width="20" height="14" viewBox="0 0 20 14"><rect width="20" height="14" fill="var(--ink)"/><path d="M0 0l10 8 10-8" stroke="#fff" stroke-width="1.5" fill="none"/></svg>drdesai@example.com</p>
  </div>
  <div class="abs" style="left:524px;top:877px">
    <p class="col-head">Obstetrics</p>
    <ul class="services">
      <li>Prenatal Care</li><li>Delivery</li><li>Postnatal checks</li><li>High Risk pregnancy</li>
    </ul>
  </div>
  <div class="abs" style="left:738px;top:877px">
    <p class="col-head">Gynaecology</p>
    <ul class="services">
      <li>Pap smears</li><li class="tall">Abnormal vaginal<br>bleeding</li><li>Fibroids</li><li>Colposcopy</li>
      <li>Family planning</li><li>Infertility</li><li class="tall">Cancer screening And<br>More....</li>
    </ul>
  </div>

  <div class="abs footer-contacts">
    <div class="contact"><svg width="22" height="22" viewBox="0 0 16 16"><circle cx="8" cy="8" r="7" fill="none" stroke="#fff" stroke-width="1"/><path d="M5.5 4.2l1.3 1.6-.8 1c.5 1 1.2 1.8 2.2 2.3l1-.8 1.6 1.3-.9 1.2c-2.6-.4-4.9-2.7-5.3-5.3z" fill="#fff"/></svg><div>General Practitioner<span>(555) 318 2207</span></div></div>
    <div class="contact"><svg width="22" height="22" viewBox="0 0 16 16"><circle cx="8" cy="8" r="7" fill="none" stroke="#fff" stroke-width="1"/><path d="M5.5 4.2l1.3 1.6-.8 1c.5 1 1.2 1.8 2.2 2.3l1-.8 1.6 1.3-.9 1.2c-2.6-.4-4.9-2.7-5.3-5.3z" fill="#fff"/></svg><div>Ophthalmologist<span>(555) 318 4452</span></div></div>
    <div class="contact"><svg width="22" height="22" viewBox="0 0 16 16"><circle cx="8" cy="8" r="7" fill="none" stroke="#fff" stroke-width="1"/><path d="M5.5 4.2l1.3 1.6-.8 1c.5 1 1.2 1.8 2.2 2.3l1-.8 1.6 1.3-.9 1.2c-2.6-.4-4.9-2.7-5.3-5.3z" fill="#fff"/></svg><div>Obstetrician/Gynaecologist<span>(555) 318 7730, (555) 462 1984</span></div></div>
  </div>

  <div class="abs hours">
    <svg width="76" height="76" viewBox="0 0 76 76" style="margin-top:10px"><circle cx="38" cy="38" r="33" fill="none" stroke="var(--ink)" stroke-width="5"/><path d="M38 16v22l10 12" stroke="var(--ink)" stroke-width="5" fill="none" stroke-linecap="round"/></svg>
    <h3>Opening hours</h3>
    <p>Monday – Fridays9am-6pm<br>Saturdays 10am – 5pm</p>
  </div>
</div>
</body>
</html>
```